Letterhead for denture company

We need a letterhead designed for our denture company called "Smilewave Dentures" We have attached the logo and business card with the colours on them that we like

Target Market(s)

Everyone aged 45+

Industry/Entity Type

Dental Clinic

Font styles to use
Serif
Sans Serif

Colors
3276b5
f37122

Requirements
Must have
• The colours used in our business card
• Be bold and modern
• Thick fonts
• Logo
Nice to have
• Elements that could tie in nicely with any future signage or website upgrades
Should not have
• Thin font
• Should not be too busy

```html
<!DOCTYPE html>
<html lang="en">
<head>
<meta charset="utf-8">
<title>Smilewave Dentures Letterhead</title>
<link href="https://fonts.googleapis.com/css2?family=Open+Sans:wght@400;600;700&display=swap" rel="stylesheet">
<style>
  :root {
    --brand-blue: #1a6bb8;
    --brand-orange: #e8601c;
    --ink: #2b2b2b;
    --muted: #8a8f96;
    --paper: #ffffff;
    --backdrop: #e9e7e4;
  }
  * { box-sizing: border-box; margin: 0; padding: 0; }
  html, body {
    width: 1200px; height: 795px; overflow: hidden;
    background: var(--backdrop);
    font-family: "Open Sans", Arial, sans-serif;
  }
  .canvas {
    width: 1200px; height: 795px;
    display: flex; align-items: center; justify-content: center;
  }
  .letterhead {
    position: relative;
    width: 537px; height: 760px;
    background: var(--paper);
    box-shadow: 0 2px 10px rgba(0,0,0,0.12);
  }
  .brand {
    position: absolute; left: 40px; top: 58px;
    display: flex; flex-direction: column; align-items: flex-start;
  }
  .brand-mark {
    width: 30px; height: 30px; background: var(--brand-blue);
    margin: 0 0 6px 36px;
  }
  .brand-name {
    font-weight: 700; font-size: 20px; color: var(--brand-blue);
    letter-spacing: 0.5px; text-transform: uppercase; line-height: 1;
  }
  .brand-tagline {
    font-weight: 600; font-size: 7.5px; color: var(--muted);
    letter-spacing: 3px; text-transform: uppercase; margin-top: 3px;
  }
  .contact {
    position: absolute; right: 40px; top: 54px;
    font-size: 8.5px; color: var(--ink); line-height: 1.45;
    list-style: none;
  }
  .contact li { display: flex; align-items: center; gap: 5px; }
  .contact .address { display: block; }
  .contact svg { width: 10px; height: 10px; flex: none; }
  .web {
    position: absolute; right: 40px; bottom: 56px;
    font-size: 9px; font-weight: 600; color: var(--ink);
  }
  .rule-orange {
    position: absolute; left: 0; right: 0; bottom: 48px;
    height: 3px; background: var(--brand-orange);
  }
  .band-blue {
    position: absolute; left: 0; right: 0; bottom: 18px;
    height: 24px; background: var(--brand-blue);
  }
</style>
</head>
<body>
<main class="canvas">
  <article class="letterhead">
    <header class="brand">
      <span class="brand-mark" aria-hidden="true"></span>
      <span class="brand-name">Smilewave Dentures</span>
      <span class="brand-tagline">The Denture Experts</span>
    </header>

    <ul class="contact">
      <li class="address">41 Harbour View Road</li>
      <li class="address">Westmere Bay, Auckland 0612</li>
      <li>
        <svg viewBox="0 0 10 10" aria-hidden="true"><circle cx="5" cy="5" r="5" fill="var(--brand-blue)"/><path d="M3.2 2.6l1 .9-.5.8c.3.7.8 1.2 1.5 1.5l.8-.5.9 1-.6.8C4.6 6.9 3 5.4 2.6 3.3z" fill="#fff"/></svg>
        0800 55 7100
      </li>
      <li>
        <svg viewBox="0 0 10 10" aria-hidden="true"><circle cx="5" cy="5" r="5" fill="var(--brand-blue)"/><rect x="2.8" y="3.6" width="4.4" height="3" rx=".4" fill="#fff"/><rect x="3.6" y="2.4" width="2.8" height="1.4" fill="#fff"/></svg>
        09 555 0142
      </li>
      <li>
        <svg viewBox="0 0 10 10" aria-hidden="true"><circle cx="5" cy="5" r="5" fill="var(--brand-blue)"/><rect x="2.6" y="3.2" width="4.8" height="3.4" fill="#fff"/><path d="M2.6 3.2L5 5.1l2.4-1.9" stroke="var(--brand-blue)" stroke-width=".6" fill="none"/></svg>
        hello@smilewavedentures.co.nz
      </li>
    </ul>

    <p class="web">www.smilewavedentures.co.nz</p>
    <div class="rule-orange"></div>
    <div class="band-blue"></div>
  </article>
</main>
</body>
</html>
```